New Company Business Card design

Looking for a corporate looking business card utilising my new logo design - the logo i would like embossed as one option and flat as another - simplistic but stylish - less is more - we are an import export business launching into the market - i would like a couple of options as main background - Grey or Black

```html
<!DOCTYPE html>
<html lang="en">
<head>
<meta charset="UTF-8">
<title>Meridian Trade Partners – Business Card</title>
<link href="https://fonts.googleapis.com/css2?family=Montserrat:wght@400;500;600&display=swap" rel="stylesheet">
<style>
  :root {
    --stage: #3a3a3a;
    --card: #1f1f1f;
    --card-front: #222222;
    --emboss: #3b3b3b;
    --brand-blue: #1a7ac4;
    --text-light: #f2f2f2;
    --divider: #8a8a8a;
  }
  * { margin: 0; padding: 0; box-sizing: border-box; }
  html, body {
    width: 1200px; height: 900px; overflow: hidden;
    background: var(--stage);
    font-family: "Montserrat", sans-serif;
  }
  .stage {
    position: relative; width: 1200px; height: 900px;
    display: flex; flex-direction: column; align-items: center; justify-content: center; gap: 40px;
  }
  .card {
    width: 700px; height: 400px;
    background: var(--card);
    position: relative;
  }
  .card--front {
    background: var(--card-front);
    display: flex; align-items: center; justify-content: center;
  }
  .brand {
    display: flex; align-items: center; gap: 14px;
    font-weight: 600; letter-spacing: 0.06em; text-transform: uppercase;
  }
  .brand__dot { width: 16px; height: 16px; border-radius: 50%; flex: none; }
  .brand--embossed { color: var(--emboss); font-size: 30px; }
  .brand--embossed .brand__dot { background: var(--emboss); }

  .card--back { display: flex; align-items: center; }
  .card__logo-side {
    width: 345px; display: flex; justify-content: center;
  }
  .brand--flat { color: var(--brand-blue); font-size: 19px; }
  .brand--flat .brand__dot { background: var(--brand-blue); width: 12px; height: 12px; }
  .card__divider {
    width: 1px; height: 200px; background: var(--divider);
  }
  .contact {
    padding-left: 42px; color: var(--text-light);
  }
  .contact__name { color: var(--brand-blue); font-weight: 600; font-size: 25px; line-height: 1.1; }
  .contact__role { font-size: 17px; margin-top: 4px; }
  .contact__address { font-size: 17px; margin-top: 18px; line-height: 1.35; }
  .contact__list { list-style: none; margin-top: 16px; font-size: 17px; }
  .contact__list li { display: flex; align-items: center; gap: 14px; line-height: 1.6; }
  .contact__icon { width: 18px; height: 18px; flex: none; }
</style>
</head>
<body>
<main class="stage">
  <section class="card card--front" aria-label="Card front">
    <div class="brand brand--embossed"><span class="brand__dot"></span>Meridian Trade Partners</div>
  </section>

  <section class="card card--back" aria-label="Card back">
    <div class="card__logo-side">
      <div class="brand brand--flat"><span class="brand__dot"></span>Meridian Trade Partners</div>
    </div>
    <div class="card__divider"></div>
    <div class="contact">
      <p class="contact__name">Daniel Whitfield</p>
      <p class="contact__role">Teaching Pastor</p>
      <p class="contact__address">412 Oak Ridge Avenue<br>Madison, MS 39110</p>
      <ul class="contact__list">
        <li>
          <svg class="contact__icon" viewBox="0 0 24 24" fill="var(--brand-blue)"><path d="M6.6 10.8a15.1 15.1 0 0 0 6.6 6.6l2.2-2.2c.3-.3.7-.4 1-.2 1.1.4 2.3.6 3.6.6.6 0 1 .4 1 1V20c0 .6-.4 1-1 1A17 17 0 0 1 3 4c0-.6.4-1 1-1h3.5c.6 0 1 .4 1 1 0 1.2.2 2.4.6 3.6.1.3 0 .7-.2 1z"/></svg>
          6015550142
        </li>
        <li>
          <svg class="contact__icon" viewBox="0 0 24 24" fill="none" stroke="var(--brand-blue)" stroke-width="1.6"><rect x="2.5" y="5" width="19" height="14"/><path d="M2.5 5l9.5 8 9.5-8"/></svg>
          daniel@meridiantrade.com
        </li>
        <li>
          <svg class="contact__icon" viewBox="0 0 24 24" fill="none" stroke="var(--brand-blue)" stroke-width="1.5"><circle cx="12" cy="12" r="9.5"/><ellipse cx="12" cy="12" rx="4.2" ry="9.5"/><path d="M2.5 12h19M4 7h16M4 17h16"/></svg>
          www.meridiantrade.com
        </li>
      </ul>
    </div>
  </section>
</main>
</body>
</html>
```